Football and Sports Management Agency Stationary

We have a logo, fonts, website and colour palette.
We need the logo refined by a proper designer and then business stationary designed. You can see on the website how it needs adjusting by a designers eye.
The company is a high end sports management company aiming to attract and represent professional athletes. The name Velorin is to indicate a 'Constellation of Stars' ie our clients. The dots on the star should be slightly different sizes to reflect that some clients will be bigger than others.
Colours:
#e6e6e6
#edd2a4
#caaa72 (main gold and also used on site)
#3f3f42
#001d38
#edeced (on website)
#191c23 (on website)
Font:
QT (velorin)
QT Melbrook (sports management)
We would like:
- Letterhead (word and indesign and PDF print format). I have attached an example for one I like. It's quiet a clean design with the contact details and address taking up only a small amount of room.
- Business card (dark on the back with the logo, personal details on the front). Only needs name, title, email, website and phone number. No company address (in PDF and indesign format)
- Powerpoint slide theme
- Logo in vector format for light and dark versions and single colour versions. And optimised web version
- Simple brand guide PDF showing colour, font and logo (a one/two page PDF)
Any questions, please ask.
NEW INFO:
Contact Details
Maren Solwick
Director
Mobile: +44 7630 218 977
Phone: +44 0113 872 604
Email: maren@velorinathletic.example
Web: velorinathletic.example
Corran Lodge, 14 Mill Bank Road, Stockport, SK4 9TW
Company number 40718362
Target Market(s)
Professional athletes, professional sports teams.
Industry/Entity Type
Management
Requirements
Must have
- NEW
- The designs must look cool, classy and high quality. My suggestion for this is to keep the text small and precise with uncomplicated design.
Nice to have
- Application of brand displayed on stationary and additional pieces of stationary branded.
- Draw some inspiration from the website. eg the slant angles used separate the sections.
Should not have
- Don't create new logos etc.

```html
<!DOCTYPE html>
<html lang="en">
<head>
<meta charset="utf-8">
<title>Velorin – Business Card</title>
<link rel="stylesheet" href="https://fonts.googleapis.com/css2?family=Work+Sans:wght@300;400;600&display=swap">
<style>
  :root {
    --stage: #e6e6e6;
    --charcoal: #3f3f42;
    --gold: #caaa72;
    --paper: #ffffff;
    --ink: #3f3f42;
    --light-text: #ffffff;
  }
  * { box-sizing: border-box; margin: 0; padding: 0; }
  html, body {
    width: 1200px; height: 900px; overflow: hidden;
    background: var(--stage);
    font-family: "Work Sans", Arial, sans-serif;
  }
  .card {
    position: absolute; left: 300px;
    width: 600px; height: 343px;
    border-radius: 18px; overflow: hidden;
    box-shadow: 0 6px 18px rgba(0,0,0,0.18);
  }
  .card--front { top: 60px; background: var(--paper); }
  .card--back { top: 497px; background: var(--charcoal); }

  .card__shapes { position: absolute; inset: 0; }

  .brand {
    position: absolute; left: 0; right: 0;
    display: flex; align-items: center; justify-content: center; gap: 18px;
    font-weight: 300; letter-spacing: 0.42em; text-transform: uppercase;
  }
  .brand__dot { width: 10px; height: 10px; border-radius: 50%; background: var(--gold); flex: none; }
  .card--front .brand { top: 62px; font-size: 36px; color: var(--ink); }
  .card--back .brand { top: 140px; font-size: 40px; color: var(--light-text); }

  .nameplate {
    position: absolute; left: 196px; top: 166px;
    width: 208px; height: 76px;
    border-radius: 22px; border: 4px solid var(--paper);
    background: var(--gold); color: var(--ink);
    text-align: center; padding-top: 11px;
  }
  .nameplate__name { font-size: 21px; font-weight: 600; line-height: 1.2; text-transform: uppercase; white-space: nowrap; }
  .nameplate__title { font-size: 15px; font-weight: 400; }

  .contact-list {
    position: absolute; left: 34px; top: 250px;
    list-style: none; color: var(--light-text); font-size: 15px; line-height: 24px;
  }
  .contact-list li { display: flex; align-items: center; gap: 9px; }
  .contact-list svg { width: 11px; height: 11px; flex: none; }
</style>
</head>
<body>

<section class="card card--front" aria-label="Business card front">
  <svg class="card__shapes" viewBox="0 0 600 343" width="600" height="343" aria-hidden="true">
    <polygon points="0,188 600,230 600,343 0,343" fill="var(--charcoal)"/>
    <line x1="0" y1="181" x2="600" y2="223" stroke="var(--gold)" stroke-width="3"/>
  </svg>

  <div class="brand"><span class="brand__dot"></span>Velorin</div>

  <div class="nameplate">
    <p class="nameplate__name">Tobin Arkwell</p>
    <p class="nameplate__title">Director</p>
  </div>

  <ul class="contact-list">
    <li>
      <svg viewBox="0 0 12 12"><path d="M3 1 L5 3.5 L3.8 5 Q5 7.5 7 8.2 L8.5 7 L11 9 L9.5 11 Q3 10 1 2.5 Z" fill="var(--gold)"/></svg>
      214.555.0163
    </li>
    <li>
      <svg viewBox="0 0 12 12"><rect x="1" y="2.5" width="10" height="7" fill="none" stroke="var(--gold)" stroke-width="1.2"/><path d="M1 2.5 L6 7 L11 2.5" fill="none" stroke="var(--gold)" stroke-width="1.2"/></svg>
      info@velorinathletic.example
    </li>
    <li>
      <svg viewBox="0 0 12 12"><circle cx="6" cy="6" r="5" fill="none" stroke="var(--gold)" stroke-width="1.2"/><ellipse cx="6" cy="6" rx="2.2" ry="5" fill="none" stroke="var(--gold)" stroke-width="1"/><line x1="1" y1="6" x2="11" y2="6" stroke="var(--gold)" stroke-width="1"/></svg>
      www.velorinathletic.example
    </li>
  </ul>
</section>

<section class="card card--back" aria-label="Business card back">
  <div class="brand"><span class="brand__dot"></span>Velorin</div>
</section>

</body>
</html>
```